We need a design for our security installation based business. Our name is K M Security Systems

We need a business card for a security installation based company. We want to look modern and professional. We would like our company logo used and the three main colours to be white, black and orange. We install intruder alarms, cctv and access control. Our preference would be to use the black/orange design on the front and orange/black on the back. Feel free to post variations.

Target Market(s)

Business owners, commercial property and large residential properties

Industry/Entity Type

Business

Contact Information for Business Card

Owen Pellworth 07812 904 226

Liam Foxcombe 07755 618 042

operations@kmsecuritysystems.example.co.uk

Intruder Alarms
CCTV
Access Control

Colors
f78f20
000000
ffffff

Requirements
Must have
• Must have the logo on the business card somewhere

```html
<!DOCTYPE html>
<html lang="en">
<head>
<meta charset="utf-8">
<title>K M Security Systems – Business Card</title>
<link rel="stylesheet" href="https://fonts.googleapis.com/css2?family=Lato:wght@400;700;900&display=swap">
<style>
  :root {
    --orange: #ee4b24;
    --black: #000000;
    --white: #ffffff;
    --backdrop: #1c1c1c;
  }
  * { margin: 0; padding: 0; box-sizing: border-box; }
  html, body {
    width: 1200px;
    height: 1200px;
    overflow: hidden;
    background: var(--backdrop);
    font-family: "Lato", sans-serif;
  }
  .canvas {
    width: 1200px;
    height: 1200px;
    display: flex;
    flex-direction: column;
    align-items: center;
    justify-content: center;
    gap: 50px;
  }
  .card {
    position: relative;
    width: 880px;
    height: 510px;
    overflow: hidden;
  }

  /* Front: orange */
  .card--front {
    background: var(--orange);
    color: var(--black);
    display: flex;
    flex-direction: column;
    align-items: center;
    justify-content: center;
  }
  .brand {
    display: flex;
    align-items: center;
    gap: 18px;
  }
  .brand__mark {
    width: 34px;
    height: 34px;
    background: currentColor;
    flex: none;
  }
  .brand__name {
    font-weight: 900;
    font-size: 50px;
    text-transform: uppercase;
    letter-spacing: 1px;
    line-height: 1;
    white-space: nowrap;
  }
  .services {
    margin-top: 40px;
    font-size: 22px;
    font-weight: 400;
    letter-spacing: 3px;
  }

  /* Back: black */
  .card--back {
    background: var(--black);
    color: var(--white);
    padding: 56px 60px;
  }
  .card--back .brand { position: relative; z-index: 1; color: var(--orange); }
  .card--back .brand__name { font-size: 46px; }
  .card--back .brand__mark { width: 30px; height: 30px; }
  .contacts {
    position: relative;
    z-index: 1;
    margin-top: 60px;
    display: flex;
    flex-direction: column;
    gap: 30px;
  }
  .contact__name {
    color: var(--orange);
    font-weight: 700;
    font-size: 34px;
    text-transform: uppercase;
    line-height: 1.1;
  }
  .contact__line {
    display: flex;
    align-items: center;
    gap: 14px;
    font-size: 26px;
    letter-spacing: 1px;
    white-space: nowrap;
  }
  .icon {
    width: 26px;
    height: 26px;
    flex: none;
  }
  .contact__email { font-size: 22px; letter-spacing: 0; }
  .decor-disc {
    position: absolute;
    right: -250px;
    bottom: -110px;
    width: 480px;
    height: 480px;
    border-radius: 50%;
    background: var(--orange);
  }
</style>
</head>
<body>
<main class="canvas">
  <section class="card card--front">
    <div class="brand">
      <span class="brand__mark"></span>
      <span class="brand__name">K M Security Systems</span>
    </div>
    <p class="services">Intruder Alarms | CCTV | Access Control</p>
  </section>

  <section class="card card--back">
    <div class="decor-disc" aria-hidden="true"></div>
    <div class="brand">
      <span class="brand__mark"></span>
      <span class="brand__name">K M Security Systems</span>
    </div>
    <div class="contacts">
      <div class="contact">
        <p class="contact__name">Liam Foxcombe</p>
        <p class="contact__line">
          <svg class="icon" viewBox="0 0 24 24" aria-hidden="true"><rect x="6" y="2" width="12" height="20" rx="2" fill="none" stroke="#ee4b24" stroke-width="2"/><line x1="10" y1="18" x2="14" y2="18" stroke="#ee4b24" stroke-width="2"/></svg>
          07755 618 042
        </p>
      </div>
      <div class="contact">
        <p class="contact__name">Owen Pellworth</p>
        <p class="contact__line">
          <svg class="icon" viewBox="0 0 24 24" aria-hidden="true"><rect x="6" y="2" width="12" height="20" rx="2" fill="none" stroke="#ee4b24" stroke-width="2"/><line x1="10" y1="18" x2="14" y2="18" stroke="#ee4b24" stroke-width="2"/></svg>
          07812 904 226
        </p>
      </div>
      <p class="contact__line contact__email">
        <svg class="icon" viewBox="0 0 24 24" aria-hidden="true"><rect x="2" y="5" width="20" height="14" rx="1" fill="none" stroke="#ee4b24" stroke-width="2"/><polyline points="2,6 12,13 22,6" fill="none" stroke="#ee4b24" stroke-width="2"/></svg>
        operations@kmsecuritysystems.example.co.uk
      </p>
    </div>
  </section>
</main>
</body>
</html>
```